Group training gym/bootcamp needs a web design

We need a website for our gym that is based in Sydney. We have indoor functional training classes and outdoor bootcamp classes. We would like the web site to have a video (to be created) and photo gallery. I would like the site made on word press and i would like to be able to make minor changes such as changing images and text without having to use a designer.

The website should have the following pages: home page; the gym; the bootcamp; photo gallery; about us; contact.

I have uploaded our logo and i would like to keep to these colour (blue,yellow,silver) and black is also allowed

Target Market(s)

18-50 male and female

Industry/Entity Type

Gym

Coding

Coded - Design and coding required

Number of Pages Required

5+ page

Font styles to use
Sans Serif

Colors
0692cd
fbed22
1b1b1b
e8e8e8

Requirements
Must have
• The website should have the following pages: home page; the gym; the bootcamp; photo gallery; about us; contact.
• I have uploaded our logo and i would like to keep to these colour (blue,yellow,silver) and black is also allowed
• Video upload and photo upload

```html
<!DOCTYPE html>
<html lang="en">
<head>
<meta charset="utf-8">
<title>Corestrong Training Hub</title>
<link href="https://fonts.googleapis.com/css2?family=Michroma&family=Open+Sans:wght@400;600;700&display=swap" rel="stylesheet">
<style>
:root{
  --blue:#0692cd;
  --yellow:#fbed22;
  --ink:#1b1b1b;
  --silver:#e8e8e8;
  --grey-band:#f4f4f4;
  --text:#555;
  --white:#fff;
}
*{box-sizing:border-box;margin:0;padding:0}
html,body{width:1200px;height:3255px;overflow:hidden;background:var(--white)}
body{position:relative;font-family:"Open Sans",Arial,sans-serif;color:var(--text)}
.abs{position:absolute}
.display{font-family:"Michroma","Arial Black",sans-serif;color:var(--ink);text-transform:uppercase}
.section-title{position:absolute;left:0;width:1200px;text-align:center;font-size:22px;letter-spacing:1px;white-space:nowrap}
.lead{position:absolute;left:220px;width:760px;text-align:center;font-size:12px;line-height:22px;color:#444}
.btn{position:absolute;background:var(--yellow);color:var(--ink);font-family:"Michroma",sans-serif;font-size:11px;text-transform:uppercase;border-radius:30px;text-align:center;white-space:nowrap}

/* header */
.site-header{position:absolute;left:0;top:0;width:1200px;height:140px;background:var(--white)}
.brand{position:absolute;left:132px;top:40px;display:flex;align-items:center;gap:12px}
.brand-mark{width:44px;height:44px;border-radius:50%;background:var(--blue)}
.brand-name{font-family:"Michroma",sans-serif;font-size:14px;line-height:20px;color:var(--blue);text-transform:uppercase;white-space:nowrap}
.call{position:absolute;left:612px;top:36px;display:flex;align-items:center;gap:8px;font-family:"Michroma",sans-serif;font-size:12.5px;color:var(--ink);white-space:nowrap}
.search{position:absolute;left:878px;top:32px;width:190px;height:32px;border:1px solid #ddd;border-radius:16px;font-size:10px;color:#aaa;padding:8px 16px;text-transform:uppercase}
.nav{position:absolute;left:0;top:92px;width:1200px;height:20px;font-family:"Michroma",sans-serif;font-size:10px;text-transform:uppercase;color:var(--ink)}
.nav a{position:absolute;top:0;color:inherit;text-decoration:none;white-space:nowrap}
.nav a.active{color:var(--blue)}

/* hero */
.hero{position:absolute;left:0;top:140px;width:1200px;height:575px;overflow:hidden}
.hero-photo{position:absolute;inset:0;background:linear-gradient(100deg,#3b3f44 0%,#6b6a66 35%,#8b7b6c 55%,#4b4c50 80%,#2c2f33 100%)}
.hero-title{position:absolute;left:130px;top:150px;font-family:"Michroma",sans-serif;text-transform:uppercase;font-weight:400;white-space:nowrap}
.hero-title .l1{font-size:34px;color:var(--yellow);display:block;line-height:50px}
.hero-title .l2{font-size:24px;color:var(--white);letter-spacing:3px;display:block;line-height:40px}
.hero-text{position:absolute;left:130px;top:248px;width:300px;font-size:12.5px;line-height:23px;color:#f0f0f0}
.arrow-btn{position:absolute;top:222px;width:40px;height:40px;border:2px solid rgba(255,255,255,.8);border-radius:50%}

/* services */
.services{position:absolute;left:0;top:710px;width:1200px}
.svc{position:absolute;top:110px;width:282px;text-align:center}
.svc-icon{display:block;margin:0 auto}
.svc-name{font-family:"Michroma",sans-serif;font-size:11px;color:var(--ink);text-transform:uppercase;margin-top:20px;white-space:nowrap}
.svc-text{font-size:11.5px;line-height:21px;color:#555;margin-top:10px}
.svc-divider{position:absolute;top:150px;width:1px;height:230px;background:#e4e4e4}

/* videos */
.videos-band{position:absolute;left:0;top:1160px;width:1200px;height:480px;background:linear-gradient(180deg,#1f2124,#2a2c2e 60%,#1b1b1b)}
.videos-title{color:var(--white)}
.videos-lead{color:#e0e0e0}
.video-frame{position:absolute;left:238px;top:1333px;width:726px;height:348px;border:3px solid var(--white);background:linear-gradient(110deg,#5c5f63,#8c8580 45%,#42464b);box-shadow:0 4px 14px rgba(0,0,0,.3)}
.play{position:absolute;left:313px;top:124px}

/* what we do */
.what-band{position:absolute;left:0;top:1905px;width:1200px;height:380px;background:var(--grey-band)}
.feature{position:absolute;top:2022px;width:450px;height:180px}
.feature-photo{position:absolute;left:0;top:0;width:180px;height:180px;border-radius:50%;border:2px dashed #cfcfcf;padding:8px}
.feature-photo div{width:100%;height:100%;border-radius:50%}
.feature-title{position:absolute;left:212px;top:0;width:240px;font-family:"Michroma",sans-serif;font-size:10.5px;line-height:24px;color:var(--ink);text-transform:uppercase}
.feature-text{position:absolute;left:212px;top:64px;width:230px;font-size:11.5px;line-height:20px;color:#555}
.feature-divider{position:absolute;left:600px;top:2022px;width:1px;height:190px;background:#e0e0e0}

/* gallery */
.gallery-tile{position:absolute}

/* newsletter */
.newsletter{position:absolute;left:0;top:2895px;width:1200px;height:100px;background:var(--blue)}
.newsletter-label{position:absolute;left:246px;top:40px;font-family:"Michroma",sans-serif;font-size:14.5px;color:var(--white);text-transform:uppercase;white-space:nowrap}
.newsletter-input{position:absolute;left:560px;top:31px;width:362px;height:40px;background:var(--white);border-radius:20px;font-size:11px;color:#555;padding:12px 20px}
.newsletter-btn{left:927px;top:31px;width:144px;height:40px;line-height:40px}

/* footer */
.site-footer{position:absolute;left:0;top:2995px;width:1200px;height:210px}
.foot-col{position:absolute;top:32px}
.foot-head{font-family:"Michroma",sans-serif;font-size:10.5px;color:var(--ink);text-transform:uppercase;margin-bottom:14px;white-space:nowrap}
.foot-list{list-style:none;font-size:11px;line-height:22px;color:#444}
.contact-row{display:flex;gap:12px;font-size:11px;line-height:16px;color:#444;margin-bottom:12px}
.social-row{display:flex;align-items:center;gap:12px;font-size:11px;color:#444;margin-bottom:8px}
.social-dot{width:32px;height:32px;border:1px solid #888;border-radius:50%}
.copyright{position:absolute;left:0;top:3208px;width:1200px;height:47px;border-top:1px solid #e4e4e4;text-align:center;font-size:11px;line-height:46px;color:#444}
.copyright .code{position:absolute;right:68px;top:0}
</style>
</head>
<body>

<header class="site-header">
  <div class="brand"><span class="brand-mark"></span><span class="brand-name">Corestrong<br>Training Hub</span></div>
  <div class="call">
    <svg width="22" height="22" viewBox="0 0 22 22"><circle cx="11" cy="11" r="10" fill="none" stroke="#0692cd" stroke-width="2"/><path d="M7 6l2.5-.5 1.3 3-1.5 1a7 7 0 0 0 3.2 3.2l1-1.5 3 1.3-.5 2.5c-5 .4-9.4-4-9-9z" fill="#0692cd"/></svg>
    CALL US 555-013-4470
  </div>
  <div class="search">Search...</div>
  <nav class="nav">
    <a class="active" style="left:414px">Home</a>
    <a style="left:493px">The Gym</a>
    <a style="left:590px">The Bootcamp</a>
    <a style="left:733px">Photo Gallery</a>
    <a style="left:881px">About Us</a>
    <a style="left:987px">Contact Us</a>
  </nav>
</header>

<section class="hero">
  <div class="hero-photo" role="img" aria-label="Trainer coaching a woman doing a dumbbell row on a bench in a gym"></div>
  <svg class="abs" style="left:0;top:0" width="1200" height="575" viewBox="0 0 1200 575">
    <path d="M0 575 Q600 420 1200 575 Z" fill="#fff"/>
    <path d="M70 572 Q600 410 1150 560" fill="none" stroke="#0692cd" stroke-width="4"/>
  </svg>
  <h1 class="hero-title"><span class="l1">Corestrong</span><span class="l2">Training Hub</span></h1>
  <p class="hero-text">Lorem ipsum dolor sit amet, consectetur adipiscing elit, sed do eiusmod tempor incididunt ut labore et dolore magna aliqua...</p>
  <div class="btn" style="left:130px;top:338px;width:176px;height:42px;line-height:42px">Learn More Info</div>
  <svg class="arrow-btn" style="left:58px" viewBox="0 0 40 40"><path d="M22 13l-7 7 7 7" fill="none" stroke="#fff" stroke-width="2"/></svg>
  <svg class="arrow-btn" style="left:1098px" viewBox="0 0 40 40"><path d="M18 13l7 7-7 7" fill="none" stroke="#fff" stroke-width="2"/></svg>
</section>

<section class="services">
  <h2 class="display section-title" style="top:0">Our Services</h2>
  <p class="lead" style="top:40px">Lorem ipsum dolor sit amet, consectetur adipiscing elit, sed do eiusmod tempor incididunt ut labore et dolore magna aliqua. Ut enim ad minim veniam, quis nostrud exercitation ullamco laboris nisi ut aliquip proident</p>

  <div class="svc" style="left:130px">
    <svg class="svc-icon" width="190" height="190" viewBox="0 0 190 190">
      <circle cx="95" cy="95" r="90" fill="none" stroke="#fbed22" stroke-width="2" opacity=".5"/>
      <path d="M95 8 A87 87 0 1 0 182 95" fill="none" stroke="#0692cd" stroke-width="8"/>
      <circle cx="95" cy="95" r="70" fill="#0692cd"/>
      <g fill="none" stroke="#fff" stroke-width="4"><rect x="58" y="72" width="10" height="46" rx="2"/><rect x="122" y="72" width="10" height="46" rx="2"/><rect x="70" y="80" width="8" height="30" rx="2"/><rect x="112" y="80" width="8" height="30" rx="2"/><path d="M78 95h34M50 95h8M132 95h8"/></g>
    </svg>
    <div class="svc-name">Accusan Doloremq</div>
    <p class="svc-text">Adipiscing elit, sed do eiusmod tempor incididunt ut labore et dolore magna aliqua. Ut enim ad minim veniam,nostrud exercitation...</p>
  </div>
  <div class="svc-divider" style="left:437px"></div>
  <div class="svc" style="left:459px">
    <svg class="svc-icon" width="190" height="190" viewBox="0 0 190 190">
      <circle cx="95" cy="95" r="90" fill="none" stroke="#fbed22" stroke-width="2" opacity=".5"/>
      <path d="M95 8 A87 87 0 0 1 182 95" fill="none" stroke="#0692cd" stroke-width="8"/>
      <circle cx="95" cy="95" r="70" fill="#0692cd"/>
      <g fill="none" stroke="#fff" stroke-width="4" stroke-linecap="round"><path d="M70 60h12l32 62"/><path d="M64 124h66"/><rect x="60" y="120" width="72" height="8" rx="3"/></g>
    </svg>
    <div class="svc-name">Accusan Doloremq</div>
    <p class="svc-text">Adipiscing elit, sed do eiusmod tempor incididunt ut labore et dolore magna aliqua. Ut enim ad minim veniam,nostrud exercitation...</p>
  </div>
  <div class="svc-divider" style="left:768px"></div>
  <div class="svc" style="left:790px">
    <svg class="svc-icon" width="190" height="190" viewBox="0 0 190 190">
      <circle cx="95" cy="95" r="90" fill="none" stroke="#fbed22" stroke-width="2" opacity=".5"/>
      <path d="M8 95 A87 87 0 0 1 95 8" fill="none" stroke="#0692cd" stroke-width="8"/>
      <circle cx="95" cy="95" r="70" fill="#0692cd"/>
      <path d="M62 128V96l14-30h18l-4 14h-10l-4 16c14-10 34-6 40 8v24z" fill="none" stroke="#fff" stroke-width="4" stroke-linejoin="round"/>
    </svg>
    <div class="svc-name">Accusan Doloremq</div>
    <p class="svc-text">Adipiscing elit, sed do eiusmod tempor incididunt ut labore et dolore magna aliqua. Ut enim ad minim veniam,nostrud exercitation...</p>
  </div>
</section>

<section>
  <div class="videos-band" role="img" aria-label="Dark blurred gym interior behind the video section"></div>
  <svg class="abs" style="left:0;top:1158px" width="1200" height="50" viewBox="0 0 1200 50"><path d="M0 0h1200v50Q600 -10 0 50z" fill="#fff"/></svg>
  <h2 class="display section-title videos-title" style="top:1203px">Our Videos</h2>
  <p class="lead videos-lead" style="top:1250px;left:290px;width:620px">Sed ut perspiciatis unde omnis iste natus error sit voluptatem accusantium doloremque laudantium, totam rem aperiam, eaque ipsa quae ab illo inventore veritatis et quasi architecto beatae vitae dict a sunt explicabo.</p>
  <svg class="abs" style="left:0;top:1600px" width="1200" height="45" viewBox="0 0 1200 45"><path d="M0 45V20Q600 -10 1200 20v25z" fill="#fff"/></svg>
  <div class="video-frame" role="img" aria-label="Video still of a trainer spotting a man doing a dumbbell press on a bench">
    <svg class="play" width="100" height="100" viewBox="0 0 100 100"><circle cx="50" cy="50" r="46" fill="rgba(0,0,0,.15)" stroke="#fff" stroke-width="5"/><path d="M40 30l28 20-28 20z" fill="#fff"/></svg>
  </div>
  <p class="lead" style="top:1712px;left:270px;width:660px">Aliquip ex ea commodo consequat. Duis aute irure dolor in reprehenderit in voluptate velit esse cillum dolore eu fugiat nulla pariatur. Excepteur sint occaecat cupidatat non proident, sunt in culpa qui officia deserunt mollit anim id est laborum numquam eius modi tempora incidunt ut labore occaecat cupidatat</p>
  <div class="btn" style="left:509px;top:1794px;width:182px;height:44px;line-height:44px;font-size:10.5px">View More Videos</div>
</section>

<section>
  <div class="what-band"></div>
  <h2 class="display section-title" style="top:1957px">What We Do</h2>
  <div class="feature" style="left:140px">
    <div class="feature-photo"><div role="img" aria-label="Woman training with suspension straps in the gym" style="background:linear-gradient(135deg,#6a5f58,#b49a86 50%,#4f5358)"></div></div>
    <div class="feature-title">Indoor Functional Training Classes</div>
    <p class="feature-text">Sed ut perspiciatis unde omnis iist natus error sit voluptatem &nbsp;loremque illum, totam rem aperiam, eaque...</p>
    <div class="btn" style="left:212px;top:148px;width:112px;height:36px;line-height:36px;font-size:10px">Read More</div>
  </div>
  <div class="feature-divider"></div>
  <div class="feature" style="left:636px">
    <div class="feature-photo"><div role="img" aria-label="Group doing plank exercises on kettlebells outdoors" style="background:linear-gradient(135deg,#8a6a5a,#c7a28a 50%,#5a4e4a)"></div></div>
    <div class="feature-title">Outdoor Bootcamp Classes</div>
    <p class="feature-text">Sed ut perspiciatis unde omnis iist natus error sit voluptatem &nbsp;loremque illum, totam rem aperiam, eaque...</p>
    <div class="btn" style="left:212px;top:148px;width:112px;height:36px;line-height:36px;font-size:10px">Read More</div>
  </div>
</section>

<section>
  <h2 class="display section-title" style="top:2340px">Photo Gallery</h2>
  <p class="lead" style="top:2381px">Lorem ipsum dolor sit amet, consectetur adipiscing elit, sed do eiusmod tempor incididunt ut labore et dolore magna aliqua. Ut enim ad minim veniam, quis nostrud exercitation ullamco laboris nisi ut aliquip proident</p>
  <div class="gallery-tile" role="img" aria-label="Black and white photo of a muscular torso holding a dumbbell" style="left:133px;top:2445px;width:299px;height:385px;background:linear-gradient(135deg,#2a2a2a,#8a8a8a 50%,#1b1b1b)">
    <div style="position:absolute;inset:10px;border:1px solid rgba(255,255,255,.8)"></div>
  </div>
  <div class="gallery-tile" role="img" aria-label="Trainer with clipboard talking to a smiling client" style="left:451px;top:2445px;width:303px;height:186px;background:linear-gradient(120deg,#6c7278,#b8a293 50%,#7d8a94)"></div>
  <div class="gallery-tile" role="img" aria-label="Woman doing a dumbbell plank row on a gym floor" style="left:770px;top:2445px;width:303px;height:186px;background:linear-gradient(120deg,#2f3236,#6d6a68 50%,#3a3d40)"></div>
  <div class="gallery-tile" role="img" aria-label="Group doing push-ups in a fitness class" style="left:451px;top:2645px;width:303px;height:185px;background:linear-gradient(120deg,#8a5e4c,#c88a6a 50%,#54484a)"></div>
  <div class="gallery-tile" role="img" aria-label="Row of people doing kettlebell planks" style="left:770px;top:2645px;width:303px;height:185px;background:linear-gradient(120deg,#3a3a3a,#9a8a80 50%,#2e2e2e)"></div>
</section>

<section class="newsletter">
  <svg class="abs" style="left:140px;top:14px" width="90" height="72" viewBox="0 0 90 72"><g fill="none" stroke="rgba(255,255,255,.25)" stroke-width="3"><path d="M6 30L84 4 70 66 44 50 6 30z"/><path d="M84 4L44 50v20l12-14"/></g></svg>
  <div class="newsletter-label">Subscribe Newsletter :</div>
  <div class="newsletter-input">Enter Your Email id :</div>
  <div class="btn newsletter-btn">Subscribe</div>
</section>

<footer class="site-footer">
  <div class="brand" style="left:132px;top:42px"><span class="brand-mark"></span><span class="brand-name">Corestrong<br>Training Hub</span></div>

  <div class="foot-col" style="left:366px">
    <div class="foot-head">Quick Links</div>
    <ul class="foot-list"><li>Home</li><li>The Gym</li><li>The Bootcamp</li><li>Photo Gallery</li><li>About us</li><li>Contact us</li></ul>
  </div>
  <div class="foot-col" style="left:536px">
    <div class="foot-head">Information</div>
    <ul class="foot-list"><li>Terms &amp; Conditions</li><li>Privacy Policy</li><li>Disclaimer</li><li>Site Map</li></ul>
  </div>
  <div class="foot-col" style="left:724px">
    <div class="foot-head">Contact Details</div>
    <div class="contact-row"><svg width="14" height="14" viewBox="0 0 14 14"><rect x="1" y="3" width="12" height="9" rx="2" fill="#444"/><rect x="4" y="1" width="6" height="3" fill="#444"/></svg>(555) 013-2290</div>
    <div class="contact-row"><svg width="14" height="14" viewBox="0 0 14 14"><rect x="1" y="3" width="12" height="9" rx="2" fill="#444"/><rect x="4" y="1" width="6" height="3" fill="#444"/></svg>(555) 013-2290</div>
    <div class="contact-row"><svg width="14" height="14" viewBox="0 0 14 14"><rect x="1" y="3" width="12" height="8" fill="none" stroke="#444" stroke-width="1.5"/><path d="M1 3l6 5 6-5" fill="none" stroke="#444" stroke-width="1.5"/></svg><span style="text-decoration:underline">hello@corestrong.example</span></div>
    <div class="contact-row"><svg width="14" height="16" viewBox="0 0 14 16"><path d="M7 1a5 5 0 0 1 5 5c0 4-5 9-5 9S2 10 2 6a5 5 0 0 1 5-5z" fill="#444"/><circle cx="7" cy="6" r="2" fill="#fff"/></svg><span>#2868 Lorem ipsum dolor sit<br>amet, consectetur</span></div>
  </div>
  <div class="foot-col" style="left:964px">
    <div class="foot-head">Follow Us</div>
    <div class="social-row"><span class="social-dot"></span>Friendbook</div>
    <div class="social-row"><span class="social-dot"></span>Chirper</div>
    <div class="social-row"><span class="social-dot"></span>Circles</div>
  </div>
</footer>

<div class="copyright">Copyrights © Corestrong Training , 2017 | All rights reserved.<span class="code">C11</span></div>

</body>
</html>
```